Business Card Design/Logo

I require a design/logo for my own Company, Morvane. The Jewellery I make is totally hand crafted. I own a hand Mining Claim out in the gemfields of Queensland and dig up my own stones. I also fossick for Gold Locally so all my Jewellery products are hand dug/cut/created. Quality stones are hand cut by my partner (Faceted) and other stones (Seconds) are either skin polished or recessed into pieces of Solid 925 Silver or Solid 9ct and 18 ct Gold. I make Sets (Collections) or just one-of designs. All the stones come in different colours and I am now starting to use different colour Golds. The final design should radiate professionalism, quality and uniqueness.

Target Market(s)

Many designs will cost a minimum of AU Dollars $2,000

Industry/Entity Type

Business

Contact Information for Business Card

Morvane Creations
Unique Hand Made Australian Jewellery
0400839627
P.O. Box 517 Tallowgrove 4718 Qld
morvanegems@quillpost.example

```html
<!DOCTYPE html>
<html lang="en">
<head>
<meta charset="utf-8">
<title>Morvane Creations – Business Card</title>
<link rel="stylesheet" href="https://fonts.googleapis.com/css2?family=Josefin+Sans:wght@300&family=Pinyon+Script&display=swap">
<style>
  :root {
    --page-bg: #e9e6e1;
    --card-center: #2b2c30;
    --card-edge: #131417;
    --gold: #d6b36a;
    --gold-soft: rgba(214, 179, 106, 0.55);
    --ink-light: #d9d3c6;
    --mark-faint: rgba(150, 150, 155, 0.16);
  }
  * { box-sizing: border-box; margin: 0; padding: 0; }
  html, body {
    width: 1200px;
    height: 1000px;
    overflow: hidden;
    background: var(--page-bg);
  }
  .canvas {
    position: relative;
    width: 1200px;
    height: 1000px;
  }
  .card {
    position: absolute;
    left: 253px;
    width: 717px;
    height: 413px;
    background: radial-gradient(ellipse at 50% 40%, var(--card-center) 0%, var(--card-edge) 85%);
    box-shadow: 0 6px 18px rgba(0, 0, 0, 0.35);
    overflow: hidden;
  }
  .card--front { top: 75px; }
  .card--back { top: 532px; }

  .brand-emblem {
    position: absolute;
    left: 303px;
    top: 85px;
    width: 110px;
    height: 110px;
  }
  .brand-name {
    font-family: "Josefin Sans", sans-serif;
    font-weight: 300;
    color: var(--gold);
    white-space: nowrap;
  }
  .tagline {
    font-family: "Pinyon Script", cursive;
    color: var(--gold);
    white-space: nowrap;
  }
  .card--front .brand-name {
    position: absolute;
    top: 260px;
    left: 0;
    width: 100%;
    text-align: center;
    font-size: 46px;
    letter-spacing: 0.5px;
  }
  .card--front .tagline {
    position: absolute;
    top: 322px;
    left: 0;
    width: 100%;
    text-align: center;
    font-size: 16px;
  }

  .back-mark {
    position: absolute;
    left: 370px;
    top: 20px;
    width: 330px;
    height: 340px;
  }
  .contact-block {
    position: absolute;
    left: 50px;
    top: 228px;
  }
  .card--back .brand-name {
    font-size: 29px;
  }
  .card--back .tagline {
    font-size: 13px;
    margin: 2px 0 0 28px;
  }
  .divider {
    width: 232px;
    height: 1px;
    margin: 8px 0 16px;
    background: linear-gradient(to right, var(--gold-soft), rgba(214, 179, 106, 0));
  }
  .contact-line {
    font-family: "Josefin Sans", sans-serif;
    font-weight: 300;
    font-size: 14.5px;
    color: var(--ink-light);
    line-height: 26px;
    white-space: nowrap;
  }
</style>
</head>
<body>
<main class="canvas">
  <section class="card card--front" aria-label="Business card front">
    <svg class="brand-emblem" viewBox="0 0 110 110" aria-hidden="true">
      <circle cx="55" cy="55" r="48" fill="none" stroke="#d6b36a" stroke-width="2"/>
    </svg>
    <h1 class="brand-name">Morvane Creations</h1>
    <p class="tagline">Unique Hand Made Australian Jewellery</p>
  </section>

  <section class="card card--back" aria-label="Business card back">
    <svg class="back-mark" viewBox="0 0 330 340" aria-hidden="true">
      <circle cx="165" cy="175" r="150" fill="var(--mark-faint)"/>
    </svg>
    <div class="contact-block">
      <h2 class="brand-name">Morvane Creations</h2>
      <p class="tagline">Unique Hand Made Australian Jewellery</p>
      <div class="divider"></div>
      <p class="contact-line">0400839627</p>
      <p class="contact-line">P.O. Box 517 Tallowgrove 4718 Qld</p>
      <p class="contact-line">morvanegems@quillpost.example</p>
    </div>
  </section>
</main>
</body>
</html>
```